Design Startseite Kanzlei-Homepage
Zielgruppe
Wir sind eine Rechtsanwaltskanzlei in Kempten (Allgäu) und regional sowie überregional in verschiedenen Rechtsgebieten tätig. Unsere Zielgruppe sind sowohl private als auch gewerbliche Mandanten.
Aufgabenstellung
Die bestehende Gestaltung wirkt derzeit aus unserer Sicht überholt. Insbesondere soll das bislang dominierende Rot vollständig entfallen.
Stattdessen stellen wir uns ein modernes, hochwertiges Erscheinungsbild vor, primär in dunklen Farbtönen (Anthrazit/Schwarz) kombiniert mit Beige- bzw. warmen Naturtönen. Ziel ist eine klare visuelle Anlehnung an unsere Kanzleiräumlichkeiten (siehe Fotos).
Die Webseite soll insgesamt moderner, klarer und visuell anspruchsvoller wirken, ohne an Seriosität und Zugänglichkeit einzubüßen. Die Balance zwischen hochwertigem Erscheinungsbild und mandantenorientierter Nutzerführung steht für uns im Vordergrund.

```html
<!DOCTYPE html>
<html lang="de">
<head>
<meta charset="utf-8">
<title>Unsere Rechtsgebiete</title>
<link href="https://fonts.googleapis.com/css2?family=Cinzel:wght@500&family=Fira+Sans+Condensed:wght@400&display=swap" rel="stylesheet">
<style>
  :root{
    --bg:#ffffff;
    --bronze:#8a6d4f;
    --card:#333333;
    --card-text:#f2f2f2;
    --heading:#8a6d4f;
  }
  *{box-sizing:border-box;margin:0;padding:0}
  html,body{width:1200px;height:686px;overflow:hidden;background:var(--bg)}
  .areas{position:relative;width:1200px;height:686px}
  .areas-title{
    position:absolute;left:214px;top:52px;
    display:flex;align-items:center;gap:8px;
    font-family:"Cinzel",serif;font-weight:500;font-size:17px;letter-spacing:.5px;
    color:var(--heading);
  }
  .areas-title::before{content:"";width:15px;height:15px;background:var(--bronze)}
  .area-grid{
    position:absolute;left:214px;top:95px;
    display:grid;grid-template-columns:repeat(3,220px);column-gap:54px;row-gap:33px;
  }
  .area-card{width:220px;height:257px;background:var(--card);color:var(--card-text)}
  .area-photo{height:125px}
  .area-head{display:flex;align-items:center;height:34px}
  .area-icon{width:34px;height:34px;background:var(--bronze);display:flex;align-items:center;justify-content:center}
  .area-icon svg{width:22px;height:22px;fill:none;stroke:#fff;stroke-width:1.3}
  .area-name{
    font-family:"Cinzel",serif;font-weight:500;font-size:17px;letter-spacing:.4px;
    margin-left:13px;color:#fff;
  }
  .area-text{
    padding:14px 17px 0 17px;
    font-family:"Fira Sans Condensed",sans-serif;font-size:9.6px;line-height:14.4px;
  }
  .photo-family{background:linear-gradient(135deg,#c9a37e,#e6c7a6 50%,#a88763)}
  .photo-labour{background:linear-gradient(135deg,#d9dde2,#f4f4f2 55%,#b9b2a4)}
  .photo-traffic{background:linear-gradient(90deg,#8d9094,#b5b8bb 60%,#6f7a55)}
  .photo-criminal{background:linear-gradient(90deg,#7b5e3c,#d8cbb5 60%,#a8b4b8)}
  .photo-inherit{background:linear-gradient(90deg,#2f4c7d,#3d5f93 55%,#6b3a28)}
  .photo-tenancy{background:linear-gradient(135deg,#e9e6e2,#ffffff 50%,#9c7a58)}
</style>
</head>
<body>
<main class="areas">
  <h2 class="areas-title">Unsere Rechtsgebiete</h2>
  <div class="area-grid">

    <article class="area-card">
      <div class="area-photo photo-family" role="img" aria-label="Foto: zwei Kinder am Tisch"></div>
      <div class="area-head">
        <span class="area-icon"><svg viewBox="0 0 24 24"><circle cx="8" cy="7" r="3"/><circle cx="16" cy="7" r="3"/><path d="M3 20v-5a5 5 0 0 1 10 0v5M11 20v-5a5 5 0 0 1 10 0v5"/></svg></span>
        <h3 class="area-name">Familienrecht</h3>
      </div>
      <p class="area-text">Lorem ipsum dolor sit amet, consectetur adipi-scing elit, sed do eiusmod tempor incididunt ut labore et dolore magna aliqua. Quis ipsum sus-pendisse ultrices gravida. Risus commodo viver-ra maecenas accumsan lacus vel facilisis.</p>
    </article>

    <article class="area-card">
      <div class="area-photo photo-labour" role="img" aria-label="Foto: Hand mit Füller beim Unterschreiben eines Vertrags"></div>
      <div class="area-head">
        <span class="area-icon"><svg viewBox="0 0 24 24"><rect x="3" y="7" width="18" height="12" rx="1"/><path d="M9 7V5h6v2M3 12h18M11 12v2h2v-2"/></svg></span>
        <h3 class="area-name">Arbeitsrecht</h3>
      </div>
      <p class="area-text">Lorem ipsum dolor sit amet, consectetur adipi-scing elit, sed do eiusmod tempor incididunt ut labore et dolore magna aliqua. Quis ipsum sus-pendisse ultrices gravida. Risus commodo viver-ra maecenas accumsan lacus vel facilisis.</p>
    </article>

    <article class="area-card">
      <div class="area-photo photo-traffic" role="img" aria-label="Foto: Autos auf der Autobahn"></div>
      <div class="area-head">
        <span class="area-icon"><svg viewBox="0 0 24 24"><path d="M12 2 22 21H2Z"/><path d="M7 17h10M8 17l1.5-3h5L16 17M8 19v-2M16 19v-2"/></svg></span>
        <h3 class="area-name">Verkehrsrecht</h3>
      </div>
      <p class="area-text">Lorem ipsum dolor sit amet, consectetur adipi-scing elit, sed do eiusmod tempor incididunt ut labore et dolore magna aliqua. Quis ipsum sus-pendisse ultrices gravida. Risus commodo viver-ra maecenas accumsan lacus vel facilisis.</p>
    </article>

    <article class="area-card">
      <div class="area-photo photo-criminal" role="img" aria-label="Foto: Justitia-Statue mit Waage"></div>
      <div class="area-head">
        <span class="area-icon"><svg viewBox="0 0 24 24"><path d="M12 3v17M8 20h8M4 6h16M6 6l-3 7a3 3 0 0 0 6 0ZM18 6l-3 7a3 3 0 0 0 6 0Z"/></svg></span>
        <h3 class="area-name">Strafrecht</h3>
      </div>
      <p class="area-text">Lorem ipsum dolor sit amet, consectetur adipi-scing elit, sed do eiusmod tempor incididunt ut labore et dolore magna aliqua. Quis ipsum sus-pendisse ultrices gravida. Risus commodo viver-ra maecenas accumsan lacus vel facilisis.</p>
    </article>

    <article class="area-card">
      <div class="area-photo photo-inherit" role="img" aria-label="Foto: Gesetzbuch und Richterhammer"></div>
      <div class="area-head">
        <span class="area-icon"><svg viewBox="0 0 24 24"><circle cx="12" cy="5" r="2.2"/><circle cx="5" cy="18" r="2.2"/><circle cx="12" cy="18" r="2.2"/><circle cx="19" cy="18" r="2.2"/><path d="M12 7v9M12 11H5v5M12 11h7v5"/></svg></span>
        <h3 class="area-name">Erbrecht</h3>
      </div>
      <p class="area-text">Lorem ipsum dolor sit amet, consectetur adipi-scing elit, sed do eiusmod tempor incididunt ut labore et dolore magna aliqua. Quis ipsum sus-pendisse ultrices gravida. Risus commodo viver-ra maecenas accumsan lacus vel facilisis.</p>
    </article>

    <article class="area-card">
      <div class="area-photo photo-tenancy" role="img" aria-label="Foto: gekündigter Mietvertrag mit Stempel und Füller"></div>
      <div class="area-head">
        <span class="area-icon"><svg viewBox="0 0 24 24"><path d="M6 2h9l4 4v16H6Z"/><path d="M15 2v4h4M9 10h7M9 13h7M9 16h5"/></svg></span>
        <h3 class="area-name">Mietrecht</h3>
      </div>
      <p class="area-text">Lorem ipsum dolor sit amet, consectetur adipi-scing elit, sed do eiusmod tempor incididunt ut labore et dolore magna aliqua. Quis ipsum sus-pendisse ultrices gravida. Risus commodo viver-ra maecenas accumsan lacus vel facilisis.</p>
    </article>

  </div>
</main>
</body>
</html>
```